Design B2B Video-Website
Zielgruppe
Das entstehende Portal bietet Videos zum Streaming an und richtet sich an Geschäftskunden, stellt also einen Shop mit Login dar. Das Angebot der Videos ist offen einsehbar, das Streamen ist gegen Bezahlung im Shop zu erwerben.
Aufgabenstellung
Die Seite soll sich im Layout an brevoqueue.com orientieren; das Farbschema angelehnt an folgende
Hexcodes:
#231f20, #60bb46 und #828282 (und ähnliche Töne). Sprache ist Deutsch.
1. Startseite/Allgemein
Die dortige Navigationsleiste oben soll etwas größer werden; wird erweitert duch ein Logo links (muss NICHT designt werden; bitte mit Platzhalter füllen); die Navigationsitems (Angebot, Preise, Über uns, FAQ, Blog), mit Farb-hover-Effekt, sollen eine Kombination aus kleine Icon und Text sein; auf der rechten Seite die Buttons "Anmelden" (nicht rot), "Login" und Suchfenster mit Lupe und "Suche". Ein Zusatzmenü wie beim Klick auf "More"
soll mitdesigned werden (Items können Platzhalter sein).
Im Hauptteil eine Box mit Auflistung von Videos (auch zum Ansehen).
Die Seite enthält ebenso einen deutlichen Footer (umfangreicher).
2. Unterseite
Inhalt der Unterseite kann beispielhaft von "Features" bzw. "Pricing" entnommen werden. Dazu hell-grauer Hintergrund (verlaufend), mit eingepassten Bildern.
"Login"-Fenster bzw. "Anmelden" ähnlich zu Brevoqueue; mehr Felder und Farbschema siehe oben.
3.Login-Bereich
Im Login-Bereich (sprich wenn der Nutzer eingeloggt ist), soll die Navigation (mit anderen Items) nach links wandern und vertikal angeordnet werden. Im Hauptinhalt(rechts von der Navigation) sollen dann die Videos oder anderen Inhalte dargestellt werden.

```html
<!DOCTYPE html>
<html lang="de">
<head>
<meta charset="utf-8">
<title>B2B Video-Portal – Anmelden</title>
<link rel="stylesheet" href="https://fonts.googleapis.com/css2?family=Open+Sans:wght@300;400;600&display=swap">
<style>
  :root {
    --ink: #231f20;
    --menu-bg: #333333;
    --green: #60bb46;
    --grey: #828282;
    --light: #efefef;
    --white: #ffffff;
    --divider: #555555;
  }
  * { box-sizing: border-box; margin: 0; padding: 0; }
  html, body { width: 1200px; height: 583px; overflow: hidden; }
  body { position: relative; font-family: "Open Sans", sans-serif; background: var(--light); color: var(--ink); }

  .mega-menu { position: absolute; left: 0; top: 0; width: 1200px; height: 187px; background: var(--menu-bg); }
  .mega-col { position: absolute; top: 24px; }
  .mega-col h3 { color: var(--green); font-weight: 400; font-size: 19px; line-height: 24px; text-decoration: underline; text-underline-offset: 3px; text-decoration-thickness: 1px; margin-bottom: 7px; }
  .mega-col li { list-style: none; color: #f2f2f2; font-weight: 300; font-size: 14px; line-height: 24px; }
  .mega-divider { position: absolute; top: 18px; width: 1px; height: 147px; background: var(--divider); }
  .close { position: absolute; left: 1178px; top: 4px; color: var(--white); font-weight: 600; font-size: 15px; }

  .main-nav { position: absolute; left: 0; top: 187px; width: 1200px; height: 77px; background: var(--white); border-bottom: 2px solid #dcdcdc; }
  .logo-placeholder { position: absolute; left: 207px; top: 20px; font-size: 25px; font-weight: 400; color: var(--ink); line-height: 36px; }
  .nav-item { position: absolute; top: 16px; width: 80px; margin-left: -40px; text-align: center; color: var(--ink); font-size: 13px; }
  .nav-item svg { display: block; margin: 0 auto 3px; width: 24px; height: 24px; }
  .nav-item.small { font-size: 11.5px; }

  .hero { position: absolute; left: 0; top: 265px; width: 1200px; height: 177px; background: var(--green); }
  .hero h1 { position: absolute; left: 147px; top: 56px; width: 600px; text-align: center; color: var(--white); font-weight: 300; font-size: 31px; line-height: 38px; }

  .signup-form { position: absolute; left: 261px; top: 484px; width: 367px; }
  .field { display: block; width: 367px; height: 33px; margin-bottom: 11px; background: var(--white); border: 1px solid #dedede; border-radius: 2px; padding-left: 9px; font-size: 13px; line-height: 31px; color: #444; }

  .product-photo { position: absolute; left: 741px; top: 287px; width: 127px; height: 300px; border-radius: 14px 14px 6px 6px; background: linear-gradient(180deg, #7d7d7d 0%, #f3efe9 22%, #d9c9b3 50%, #b59a7b 80%, #e5e0da 100%); }
</style>
</head>
<body>
  <nav class="mega-menu" aria-label="Zusatzmenü">
    <div class="mega-col" style="left:91px"><h3>LOREM IPSUM</h3><ul><li>Lorem ipsum dolor</li><li>Lorem ipsum dolor</li><li>Lorem ipsum dolor</li></ul></div>
    <div class="mega-divider" style="left:293px"></div>
    <div class="mega-col" style="left:382px"><h3>LOREM IPSUM</h3><ul><li>Consetetur sadipscing</li><li>Consetetur sadipscing</li><li>Consetetur sadipscing</li><li>Consetetur sadipscing</li></ul></div>
    <div class="mega-divider" style="left:603px"></div>
    <div class="mega-col" style="left:675px"><h3>LOREM IPSUM</h3><ul><li>Lorem ipsum dolor</li><li>Lorem ipsum dolor</li><li>Lorem ipsum dolor</li></ul></div>
    <div class="mega-divider" style="left:889px"></div>
    <div class="mega-col" style="left:967px"><h3>LOREM IPSUM</h3><ul><li>Consetetur sadipscing</li><li>Consetetur sadipscing</li><li>Consetetur sadipscing</li><li>Consetetur sadipscing</li></ul></div>
    <span class="close">X</span>
  </nav>

  <header class="main-nav">
    <div class="logo-placeholder">MyLogo</div>
    <div class="nav-item" style="left:360px"><svg viewBox="0 0 24 24" fill="none" stroke="#60bb46" stroke-width="1.4"><path d="M12 4 22 9 12 14 2 9Z"/><path d="M2 12l10 5 10-5M2 15l10 5 10-5"/></svg>Angebot</div>
    <div class="nav-item" style="left:436px"><svg viewBox="0 0 24 24" fill="none" stroke="#60bb46" stroke-width="1.5"><rect x="4" y="2" width="16" height="20" rx="1"/><rect x="7" y="5" width="10" height="4"/><path d="M8 12h1M11.5 12h1M15 12h1M8 15h1M11.5 15h1M15 15h1M8 18h1M11.5 18h1M15 18h1" stroke-width="2"/></svg>Preise</div>
    <div class="nav-item" style="left:519px"><svg viewBox="0 0 24 24" fill="#60bb46"><circle cx="14" cy="4" r="2.4"/><path d="M10 9h5l-3 10h3l-1 2H8l3-10H9z"/></svg>Über uns</div>
    <div class="nav-item" style="left:593px"><svg viewBox="0 0 24 24" fill="none" stroke="#60bb46" stroke-width="3"><path d="M7 8a5 5 0 1 1 7 4.5c-1.5.8-2 1.5-2 3.5"/><circle cx="12" cy="21" r="0.6" fill="#60bb46"/></svg>FAQ</div>
    <div class="nav-item" style="left:659px"><svg viewBox="0 0 24 24" fill="none" stroke="#60bb46" stroke-width="1.5"><path d="M17 3l4 4L9 19l-5 1 1-5z"/><path d="M15 5l4 4"/></svg>Blog</div>
    <div class="nav-item small" style="left:774px"><svg viewBox="0 0 24 24" fill="#60bb46"><circle cx="12" cy="7" r="4.5"/><path d="M4 22c0-6 3.5-9 8-9s8 3 8 9z"/></svg>Anmelden</div>
    <div class="nav-item small" style="left:843px"><svg viewBox="0 0 24 24" fill="#60bb46"><path d="M7 11V8a5 5 0 0 1 10 0v3h-2V8a3 3 0 0 0-6 0v3z"/><rect x="5" y="11" width="14" height="11" rx="1"/></svg>Login</div>
    <div class="nav-item small" style="left:905px"><svg viewBox="0 0 24 24" fill="none" stroke="#60bb46"><circle cx="9" cy="9" r="5.5" stroke-width="2.6"/><path d="M13 13l8 8" stroke-width="3.5"/></svg>Suche</div>
  </header>

  <section class="hero">
    <h1>Jetzt Anmelden<br>Portal für komplexe B2B Videos</h1>
  </section>

  <form class="signup-form">
    <span class="field">Firma</span>
    <span class="field">Vorname</span>
    <span class="field"></span>
  </form>

  <div class="product-photo" role="img" aria-label="Foto eines Glases Eiskaffee mit Sahne und Löffel"></div>
</body>
</html>
```